Reproduce my app screenshot to look more updated and modern

My app is a place for farmers to post jobs a when needing help around the Farm, and local farmhands can apply for the job. The Farmer can then review multiple applicants and select the one best fit for the task at hand. I'm trying to give my screens an updated look while keeping my current color scheme and flow. I would like for you guys to recreate this screen with an updated loo the best you can. The main screen with the QV will stay the same. I put that in there to show our logo and our main colors. They look outdated.

Target Market(s)

Farmers and Farm Emlpoyees inside the US

Industry/Entity Type

Agriculture

Requirements
Must have
• and updated look and same buttom/ functionality
Nice to have
Should not have
• dont change the name of any buttons

```html
<!DOCTYPE html>
<html lang="en">
<head>
<meta charset="utf-8">
<title>Fieldmate – App Screens</title>
<link rel="stylesheet" href="https://fonts.googleapis.com/css2?family=Open+Sans:wght@400;500;600;700;800&display=swap">
<style>
:root{
  --page:#e4e6e2;
  --surface:#ffffff;
  --surface-soft:#f5f7f3;
  --green:#5d9b48;
  --green-deep:#3c6b34;
  --green-text:#3f8a2e;
  --green-tint:#e6f1df;
  --green-tint-2:#f0f6ec;
  --splash-top:#9bcb55;
  --splash-bottom:#5fa846;
  --ink:#1f2a1c;
  --ink-soft:#3d463a;
  --muted:#8d958a;
  --line:#e6e9e3;
  --heart:#e04848;
  --heart-off:#c5cac2;
  --star:#f5b83d;
  --shadow:0 6px 18px rgba(40,60,30,.10);
  --card-shadow:0 2px 8px rgba(40,60,30,.07);
}
*{box-sizing:border-box;margin:0;padding:0}
html,body{width:761px;height:1200px;overflow:hidden}
body{background:var(--page);font-family:"Open Sans",Arial,sans-serif;color:var(--ink);position:relative}
.abs{position:absolute}
.screen{position:absolute;width:278px;height:495px;background:var(--surface-soft);border-radius:18px;box-shadow:var(--shadow);overflow:hidden}

/* ---------- splash ---------- */
.splash{left:86px;top:102px;background:linear-gradient(165deg,var(--splash-top),var(--splash-bottom))}
.splash-glow{left:-60px;top:-80px;width:260px;height:260px;border-radius:50%;background:rgba(255,255,255,.10)}
.splash-glow-2{left:120px;top:360px;width:240px;height:240px;border-radius:50%;background:rgba(255,255,255,.07)}
.splash-mark{left:94px;top:168px;width:90px;height:90px;border-radius:26px;background:var(--green-deep);border:4px solid #cdeb94;box-shadow:0 10px 24px rgba(30,60,20,.28)}
.splash-name{left:0;width:278px;top:282px;text-align:center;color:#fff;font-weight:800;font-size:25px;letter-spacing:1.5px}

/* ---------- shared header ---------- */
.topbar{left:0;top:0;width:100%;height:46px;background:var(--surface)}
.page-title{font-weight:700;font-size:11px;color:var(--ink)}
.back-btn{width:24px;height:24px;border-radius:50%;background:var(--surface-soft);display:flex;align-items:center;justify-content:center}
.avatar{border-radius:50%;background:linear-gradient(150deg,#c99a5c,#6b4a2c)}
.online{width:7px;height:7px;border-radius:50%;background:#6dc04a;border:1.5px solid #fff}

/* ---------- home ---------- */
.home{left:381px;top:102px}
.home-head{left:0;top:0;width:100%;height:112px;background:var(--surface);border-radius:0 0 18px 18px;box-shadow:0 2px 6px rgba(40,60,30,.05)}
.segmented{left:14px;top:46px;width:250px;height:24px;border-radius:12px;background:var(--surface-soft);display:flex;padding:2px}
.segment{flex:1;border-radius:10px;font-size:8px;display:flex;align-items:center;justify-content:center;color:var(--muted);font-weight:600}
.segment.is-active{background:var(--green);color:#fff;box-shadow:0 2px 6px rgba(93,155,72,.35)}
.search{left:14px;top:78px;width:222px;height:24px;background:var(--surface-soft);border-radius:12px}
.search-text{left:26px;top:6px;font-size:7.5px;color:var(--muted)}
.filter-btn{left:240px;top:78px;width:24px;height:24px;border-radius:12px;background:var(--green-tint);display:flex;align-items:center;justify-content:center}

.job-card{left:14px;width:250px;height:72px;background:var(--surface);border-radius:12px;box-shadow:var(--card-shadow)}
.job-icon{left:10px;top:9px;width:32px;height:32px;border-radius:10px;background:var(--green-tint);display:flex;align-items:center;justify-content:center}
.job-title{left:52px;top:8px;font-size:9.5px;font-weight:700;color:var(--green-text);white-space:nowrap}
.job-meta{left:52px;top:22px;font-size:6.5px;color:var(--muted);white-space:nowrap;line-height:9px}
.heart-btn{left:222px;top:9px;width:20px;height:20px;border-radius:50%;background:var(--surface-soft);display:flex;align-items:center;justify-content:center}
.job-divider{left:10px;top:47px;width:230px;height:1px;background:var(--line)}
.job-rate{left:10px;top:54px;font-size:6.5px;color:var(--muted);display:flex;align-items:center;gap:4px;white-space:nowrap}
.rate-chip{background:var(--green-tint);color:var(--green-text);font-weight:700;border-radius:7px;padding:1px 6px}
.job-dates{left:156px;top:51px;width:84px;font-size:6px;color:var(--muted);line-height:8px}
.job-dates span{display:flex;justify-content:space-between;white-space:nowrap}

.nav{left:12px;top:446px;width:254px;height:38px;background:var(--surface);border-radius:19px;box-shadow:0 4px 14px rgba(40,60,30,.16);display:flex;align-items:center;justify-content:space-around;padding:0 8px}
.nav-item{width:28px;height:28px;border-radius:50%;display:flex;align-items:center;justify-content:center}
.nav-item.is-active{background:var(--green)}
.nav-item svg{width:15px;height:15px}

/* ---------- profile ---------- */
.profile{left:88px;top:612px}
.profile-card{left:14px;top:54px;width:250px;height:72px;border-radius:14px;background:linear-gradient(135deg,#6aa954,var(--green-deep));box-shadow:0 6px 14px rgba(60,107,52,.28)}
.profile-name{left:64px;top:15px;color:#fff;font-weight:700;font-size:12px;white-space:nowrap}
.profile-role{left:64px;top:33px;color:rgba(255,255,255,.9);font-size:7.5px;line-height:10px;font-weight:600}
.rating{left:206px;top:14px;height:16px;padding:0 6px;border-radius:8px;background:rgba(255,255,255,.2);color:#fff;font-size:7.5px;font-weight:600;display:flex;align-items:center;gap:3px}
.menu-group{left:14px;width:250px;background:var(--surface);border-radius:12px;box-shadow:var(--card-shadow);padding:0 12px}
.menu-row{height:21px;display:flex;justify-content:space-between;align-items:center;border-bottom:1px solid var(--line)}
.menu-row:last-child{border-bottom:none}
.menu-label{font-size:8.5px;color:var(--ink-soft);font-weight:500}
.menu-link{font-size:6.5px;color:var(--muted);display:flex;align-items:center;gap:5px}
.menu-link svg{width:5px;height:8px}
.section-title{left:18px;top:229px;font-size:9px;font-weight:700;color:var(--green-text)}
.btn{left:14px;width:250px;height:28px;border-radius:14px;background:var(--green);color:#fff;font-size:8.5px;font-weight:600;display:flex;align-items:center;justify-content:center;box-shadow:0 4px 10px rgba(93,155,72,.35)}

/* ---------- create job ---------- */
.create{left:381px;top:612px}
.brand-small{left:14px;top:56px;font-weight:800;font-size:13px;color:var(--green-deep);letter-spacing:.5px}
.brand-line{left:14px;top:76px;width:250px;height:1px;background:var(--line)}
.field{left:14px;width:250px;height:28px;background:var(--surface);border:1px solid var(--line);border-radius:10px;display:flex;align-items:center;padding:0 10px}
.field-icon{width:16px;height:16px;border-radius:5px;background:var(--green-tint);display:flex;align-items:center;justify-content:center;margin-right:7px}
.field-icon svg{width:9px;height:8px}
.field-label{font-size:7.5px;color:var(--muted);flex:1}
.chev{width:7px;height:5px}
.pay-options{left:14px;top:164px;width:250px;display:flex;gap:6px}
.pay-chip{flex:1;height:22px;border-radius:11px;background:var(--surface);border:1px solid var(--line);font-size:7px;color:var(--muted);display:flex;align-items:center;justify-content:center;gap:4px;white-space:nowrap}
.pay-chip i{width:6px;height:6px;border-radius:50%;border:1px solid #b7bdb3;display:block}
.pay-chip.is-selected{background:var(--green-tint);border-color:#bcd9ae;color:var(--green-text);font-weight:600}
.pay-chip.is-selected i{border:2px solid var(--green);background:#fff}
.range{top:196px;width:122px;height:28px;background:var(--surface);border:1px solid var(--line);border-radius:10px;font-size:7.5px;color:var(--muted);padding:8px 10px}
</style>
</head>
<body>

<!-- Splash -->
<section class="screen splash" aria-label="Splash screen">
  <div class="abs splash-glow"></div>
  <div class="abs splash-glow-2"></div>
  <div class="abs splash-mark"></div>
  <div class="abs splash-name">QV FIELDMATE</div>
</section>

<!-- Home -->
<section class="screen home" aria-label="Home screen">
  <div class="abs home-head"></div>
  <div class="abs page-title" style="left:16px;top:15px;font-size:13px">Home</div>
  <div class="abs avatar" role="img" aria-label="User profile photo" style="left:236px;top:10px;width:28px;height:28px"></div>
  <div class="abs online" style="left:257px;top:10px"></div>

  <div class="abs segmented">
    <div class="segment is-active">Current Jobs For You</div>
    <div class="segment">Nearby Farmhands</div>
  </div>

  <div class="abs search">
    <svg class="abs" style="left:10px;top:7px" width="10" height="10" viewBox="0 0 10 10"><circle cx="4" cy="4" r="3" fill="none" stroke="#8d958a" stroke-width="1.3"/><path d="M6.3 6.3 9 9" stroke="#8d958a" stroke-width="1.3" stroke-linecap="round"/></svg>
    <div class="abs search-text">search</div>
  </div>
  <div class="abs filter-btn"><svg width="10" height="8" viewBox="0 0 10 8"><path d="M0 1h10M2 4h6M4 7h2" stroke="#3f8a2e" stroke-width="1.3" stroke-linecap="round"/></svg></div>

  <!-- card 1 -->
  <article class="abs job-card" style="top:116px">
    <div class="abs job-icon"><svg width="15" height="14" viewBox="0 0 16 15" fill="none" stroke="#5d9b48" stroke-width="1.4"><rect x="1.5" y="4" width="13" height="9" rx="2"/><path d="M6 4V2.5h4V4M1.5 8h13"/></svg></div>
    <div class="abs job-title">Seasional Farm Labour</div>
    <div class="abs job-meta">Pine Hollow, Iowa<br>2.92 Miles &nbsp;·&nbsp; 08:00am - 08:00pm</div>
    <div class="abs heart-btn"><svg width="11" height="10" viewBox="0 0 24 21"><path d="M12 21 2 11C-1 8 0 2 6 1c3 0 5 2 6 4 1-2 3-4 6-4 6 1 7 7 4 10z" fill="var(--heart)"/></svg></div>
    <div class="abs job-divider"></div>
    <div class="abs job-rate">Hourly Rate <span class="rate-chip">$12 - 20</span></div>
    <div class="abs job-dates"><span><em style="font-style:normal">Start Date:</em><em style="font-style:normal">April 01</em></span><span><em style="font-style:normal">End Date:</em><em style="font-style:normal">December 15</em></span></div>
  </article>

  <!-- card 2 -->
  <article class="abs job-card" style="top:196px">
    <div class="abs job-icon"><svg width="16" height="13" viewBox="0 0 17 14" fill="none" stroke="#5d9b48" stroke-width="1.3"><path d="M1 3h9v7H1zM10 5h3l3 3v2h-6"/><circle cx="4" cy="11" r="1.6"/><circle cx="13" cy="11" r="1.6"/></svg></div>
    <div class="abs job-title">Truck Driver</div>
    <div class="abs job-meta">Pine Hollow, Iowa<br>2.92 Miles &nbsp;·&nbsp; 08:00am - 08:00pm</div>
    <div class="abs heart-btn"><svg width="11" height="10" viewBox="0 0 24 21"><path d="M12 21 2 11C-1 8 0 2 6 1c3 0 5 2 6 4 1-2 3-4 6-4 6 1 7 7 4 10z" fill="var(--heart-off)"/></svg></div>
    <div class="abs job-divider"></div>
    <div class="abs job-rate">Hourly Rate <span class="rate-chip">$12 - 20</span></div>
    <div class="abs job-dates"><span><em style="font-style:normal">Start Date:</em><em style="font-style:normal">March 01</em></span><span><em style="font-style:normal">End Date:</em><em style="font-style:normal">Feburary 28</em></span></div>
  </article>

  <!-- card 3 -->
  <article class="abs job-card" style="top:276px">
    <div class="abs job-icon"><svg width="14" height="14" viewBox="0 0 15 16" fill="none" stroke="#5d9b48" stroke-width="1.4" stroke-linecap="round"><path d="M3 15V6M6 15V2M9 15V3M12 15V7M2 15h11"/></svg></div>
    <div class="abs job-title">Farm Hand, Sprayer, Truck</div>
    <div class="abs job-meta">Pine Hollow, Iowa<br>6.09 Miles &nbsp;·&nbsp; 08:00am - 08:00pm</div>
    <div class="abs heart-btn"><svg width="11" height="10" viewBox="0 0 24 21"><path d="M12 21 2 11C-1 8 0 2 6 1c3 0 5 2 6 4 1-2 3-4 6-4 6 1 7 7 4 10z" fill="var(--heart-off)"/></svg></div>
    <div class="abs job-divider"></div>
    <div class="abs job-rate">Hourly Rate <span class="rate-chip">$16 - 22</span></div>
    <div class="abs job-dates"><span><em style="font-style:normal">Start Date:</em><em style="font-style:normal">April 01</em></span><span><em style="font-style:normal">End Date:</em><em style="font-style:normal">December 15</em></span></div>
  </article>

  <!-- card 4 -->
  <article class="abs job-card" style="top:356px">
    <div class="abs job-icon"><svg width="15" height="14" viewBox="0 0 16 15" fill="none" stroke="#5d9b48" stroke-width="1.4"><rect x="1.5" y="4" width="13" height="9" rx="2"/><path d="M6 4V2.5h4V4M1.5 8h13"/></svg></div>
    <div class="abs job-title">Sort And Lord Pigs</div>
    <div class="abs job-meta">Pine Hollow, Iowa<br>6.09 Miles &nbsp;·&nbsp; 08:00am - 08:00pm</div>
    <div class="abs heart-btn"><svg width="11" height="10" viewBox="0 0 24 21"><path d="M12 21 2 11C-1 8 0 2 6 1c3 0 5 2 6 4 1-2 3-4 6-4 6 1 7 7 4 10z" fill="var(--heart-off)"/></svg></div>
    <div class="abs job-divider"></div>
    <div class="abs job-rate">Hourly Rate <span class="rate-chip">$16 - 22</span></div>
    <div class="abs job-dates"><span><em style="font-style:normal">Start Date:</em><em style="font-style:normal">April 01</em></span><span><em style="font-style:normal">End Date:</em><em style="font-style:normal">December 15</em></span></div>
  </article>

  <!-- card 5 -->
  <article class="abs job-card" style="top:436px">
    <div class="abs job-icon"><svg width="14" height="14" viewBox="0 0 15 16" fill="none" stroke="#5d9b48" stroke-width="1.4" stroke-linecap="round"><path d="M3 15V6M6 15V2M9 15V3M12 15V7M2 15h11"/></svg></div>
    <div class="abs job-title">Farm Hand, Sprayer, Truck</div>
    <div class="abs job-meta">Pine Hollow, Iowa<br>6.09 Miles &nbsp;·&nbsp; 08:00am - 08:00pm</div>
    <div class="abs heart-btn"><svg width="11" height="10" viewBox="0 0 24 21"><path d="M12 21 2 11C-1 8 0 2 6 1c3 0 5 2 6 4 1-2 3-4 6-4 6 1 7 7 4 10z" fill="var(--heart-off)"/></svg></div>
  </article>

  <nav class="abs nav" aria-label="Main navigation">
    <div class="nav-item is-active"><svg viewBox="0 0 18 18"><path d="M9 2 1.5 8.5h2.5V16h3.5v-4.5h3V16h3.5V8.5h2.5z" fill="#fff"/></svg></div>
    <div class="nav-item"><svg viewBox="0 0 18 18" fill="none" stroke="#8d958a" stroke-width="1.8" stroke-linecap="round"><circle cx="7.5" cy="7.5" r="5"/><path d="m11.5 11.5 4.5 4.5"/></svg></div>
    <div class="nav-item"><svg viewBox="0 0 18 18" fill="none" stroke="#8d958a" stroke-width="1.5" stroke-linecap="round"><rect x="5" y="2.5" width="11" height="14" rx="2"/><path d="M2 5v10.5h2.5M8 7h5M8 10h5M8 13h3"/></svg></div>
    <div class="nav-item"><svg viewBox="0 0 18 18" fill="none" stroke="#8d958a" stroke-width="1.5" stroke-linecap="round"><path d="M5 16V7M8 16V3M11 16V4M14 16V8M3.5 16h12"/></svg></div>
    <div class="nav-item"><svg viewBox="0 0 18 18" fill="none" stroke="#8d958a" stroke-width="1.4" stroke-linecap="round"><rect x="1.5" y="3" width="13" height="12" rx="2"/><path d="M1.5 6.5h13M5 1.5v3M11 1.5v3"/><circle cx="13.5" cy="13.5" r="3.5" fill="#fff"/><path d="M13.5 11.8v1.8h1.4"/></svg></div>
  </nav>
</section>

<!-- My Profile -->
<section class="screen profile" aria-label="My Profile screen">
  <div class="abs topbar"></div>
  <div class="abs back-btn" style="left:14px;top:11px"><svg width="6" height="9" viewBox="0 0 6 9"><path d="M5 1 1.5 4.5 5 8" fill="none" stroke="#1f2a1c" stroke-width="1.4" stroke-linecap="round"/></svg></div>
  <div class="abs page-title" style="left:46px;top:15px">My Profile</div>

  <div class="abs profile-card">
    <div class="abs avatar" role="img" aria-label="Profile photo" style="left:12px;top:14px;width:44px;height:44px;border:2px solid #fff"></div>
    <div class="abs online" style="left:46px;top:14px;width:9px;height:9px"></div>
    <div class="abs profile-name">Daniel Hartwell</div>
    <div class="abs profile-role">Founder \ C.E.O<br>5550148823</div>
    <div class="abs rating"><svg width="9" height="9" viewBox="0 0 10 10"><path d="m5 .5 1.4 3 3.1.3-2.4 2.1.8 3.1L5 7.4 2.1 9l.8-3.1L.5 3.8l3.1-.3z" fill="var(--star)"/></svg>5.0</div>
  </div>

  <div class="abs menu-group" style="top:136px">
    <div class="menu-row"><span class="menu-label">User Details</span><span class="menu-link">View Details<svg viewBox="0 0 5 8"><path d="m1 1 3 3-3 3" fill="none" stroke="var(--green)" stroke-width="1.3" stroke-linecap="round"/></svg></span></div>
    <div class="menu-row"><span class="menu-label">Education Details</span><span class="menu-link">View Details<svg viewBox="0 0 5 8"><path d="m1 1 3 3-3 3" fill="none" stroke="var(--green)" stroke-width="1.3" stroke-linecap="round"/></svg></span></div>
    <div class="menu-row"><span class="menu-label">Farm Details</span><span class="menu-link">View Details<svg viewBox="0 0 5 8"><path d="m1 1 3 3-3 3" fill="none" stroke="var(--green)" stroke-width="1.3" stroke-linecap="round"/></svg></span></div>
    <div class="menu-row"><span class="menu-label">Farm Images</span><span class="menu-link">View Details<svg viewBox="0 0 5 8"><path d="m1 1 3 3-3 3" fill="none" stroke="var(--green)" stroke-width="1.3" stroke-linecap="round"/></svg></span></div>
  </div>

  <div class="abs section-title">Fieldmate Jobs</div>

  <div class="abs menu-group" style="top:246px">
    <div class="menu-row"><span class="menu-label">Applied Jobs</span><span class="menu-link">View Details<svg viewBox="0 0 5 8"><path d="m1 1 3 3-3 3" fill="none" stroke="var(--green)" stroke-width="1.3" stroke-linecap="round"/></svg></span></div>
    <div class="menu-row"><span class="menu-label">Scheduled Jobs</span><span class="menu-link">View Details<svg viewBox="0 0 5 8"><path d="m1 1 3 3-3 3" fill="none" stroke="var(--green)" stroke-width="1.3" stroke-linecap="round"/></svg></span></div>
    <div class="menu-row"><span class="menu-label">Received Jobs</span><span class="menu-link">View Details<svg viewBox="0 0 5 8"><path d="m1 1 3 3-3 3" fill="none" stroke="var(--green)" stroke-width="1.3" stroke-linecap="round"/></svg></span></div>
    <div class="menu-row"><span class="menu-label">Favourite Jobs</span><span class="menu-link">View Details<svg viewBox="0 0 5 8"><path d="m1 1 3 3-3 3" fill="none" stroke="var(--green)" stroke-width="1.3" stroke-linecap="round"/></svg></span></div>
    <div class="menu-row"><span class="menu-label">Completed Jobs</span><span class="menu-link">View Details<svg viewBox="0 0 5 8"><path d="m1 1 3 3-3 3" fill="none" stroke="var(--green)" stroke-width="1.3" stroke-linecap="round"/></svg></span></div>
    <div class="menu-row"><span class="menu-label">Scheduled Jobs</span><span class="menu-link">View Details<svg viewBox="0 0 5 8"><path d="m1 1 3 3-3 3" fill="none" stroke="var(--green)" stroke-width="1.3" stroke-linecap="round"/></svg></span></div>
    <div class="menu-row"><span class="menu-label">Received Jobs</span><span class="menu-link">View Details<svg viewBox="0 0 5 8"><path d="m1 1 3 3-3 3" fill="none" stroke="var(--green)" stroke-width="1.3" stroke-linecap="round"/></svg></span></div>
  </div>

  <div class="abs btn" style="top:452px">Logout</div>
</section>

<!-- Create New Job -->
<section class="screen create" aria-label="Create New Job screen">
  <div class="abs topbar"></div>
  <div class="abs back-btn" style="left:14px;top:11px"><svg width="6" height="9" viewBox="0 0 6 9"><path d="M5 1 1.5 4.5 5 8" fill="none" stroke="#1f2a1c" stroke-width="1.4" stroke-linecap="round"/></svg></div>
  <div class="abs page-title" style="left:46px;top:15px">Create New Job</div>

  <div class="abs brand-small">QV FIELDMATE</div>
  <div class="abs brand-line"></div>

  <div class="abs field" style="top:86px"><span class="field-icon"><svg viewBox="0 0 11 9" fill="none" stroke="var(--green)" stroke-width="1.1"><rect x=".5" y="2" width="10" height="6.5" rx="1"/><path d="M3.5 2V.8h4V2M.5 5h10"/></svg></span><span class="field-label">Job Category</span><svg class="chev" viewBox="0 0 7 5"><path d="m1 1 2.5 2.5L6 1" fill="none" stroke="#8d958a" stroke-width="1.2" stroke-linecap="round"/></svg></div>
  <div class="abs field" style="top:124px"><span class="field-icon"><svg viewBox="0 0 11 9" fill="none" stroke="var(--green)" stroke-width="1.1"><rect x=".5" y="2" width="10" height="6.5" rx="1"/><path d="M3.5 2V.8h4V2M.5 5h10"/></svg></span><span class="field-label">Job Title</span><svg class="chev" viewBox="0 0 7 5"><path d="m1 1 2.5 2.5L6 1" fill="none" stroke="#8d958a" stroke-width="1.2" stroke-linecap="round"/></svg></div>

  <div class="abs pay-options">
    <div class="pay-chip is-selected"><i></i>Hourly Rate ($)</div>
    <div class="pay-chip"><i></i>Fixed Salary ($)</div>
    <div class="pay-chip"><i></i>Per Acre ($)</div>
  </div>

  <div class="abs range" style="left:14px">From</div>
  <div class="abs range" style="left:142px">To</div>

  <div class="abs field" style="top:238px"><span class="field-icon"><svg viewBox="0 0 11 9" fill="none" stroke="var(--green)" stroke-width="1.1"><rect x=".5" y="2" width="10" height="6.5" rx="1"/><path d="M3.5 2V.8h4V2M.5 5h10"/></svg></span><span class="field-label">Job Type</span><svg class="chev" viewBox="0 0 7 5"><path d="m1 1 2.5 2.5L6 1" fill="none" stroke="#8d958a" stroke-width="1.2" stroke-linecap="round"/></svg></div>
  <div class="abs field" style="top:276px"><span class="field-icon"><svg viewBox="0 0 11 9" fill="none" stroke="var(--green)" stroke-width="1.1"><rect x=".5" y="2" width="10" height="6.5" rx="1"/><path d="M3.5 2V.8h4V2M.5 5h10"/></svg></span><span class="field-label">Equipment Provided</span><svg class="chev" viewBox="0 0 7 5"><path d="m1 1 2.5 2.5L6 1" fill="none" stroke="#8d958a" stroke-width="1.2" stroke-linecap="round"/></svg></div>
  <div class="abs field" style="top:314px"><span class="field-icon"><svg viewBox="0 0 11 9" fill="none" stroke="var(--green)" stroke-width="1.1"><rect x=".5" y="2" width="10" height="6.5" rx="1"/><path d="M3.5 2V.8h4V2M.5 5h10"/></svg></span><span class="field-label">Start Date and Time</span><svg class="chev" viewBox="0 0 7 5"><path d="m1 1 2.5 2.5L6 1" fill="none" stroke="#8d958a" stroke-width="1.2" stroke-linecap="round"/></svg></div>
  <div class="abs field" style="top:352px"><span class="field-icon"><svg viewBox="0 0 11 9" fill="none" stroke="var(--green)" stroke-width="1.1"><rect x=".5" y="2" width="10" height="6.5" rx="1"/><path d="M3.5 2V.8h4V2M.5 5h10"/></svg></span><span class="field-label">End Date and Time</span><svg class="chev" viewBox="0 0 7 5"><path d="m1 1 2.5 2.5L6 1" fill="none" stroke="#8d958a" stroke-width="1.2" stroke-linecap="round"/></svg></div>

  <div class="abs btn" style="top:448px">Logout</div>
</section>

</body>
</html>
```